Brolga Ridge Earthmoving & Transport Business Card

Can you please design a business card for an Earthworks, Haulage truck and machinery hire company. They also provide sand soil and mulch supply, as well as screening of products. Can you re-create the logo from the attached but add Brolga Ridge Earthmoving & Transport just use the three diamond design.

Target Market(s)

Earthmoving and Transport, Landscapers, Construction

Contact Information for Business Card

ABN 52 907 338 214, Dale Pettigrew, Managing Director, Brolga Ridge Earthmoving & Transport Mobile 0438 256 904 Email brgtransport2011@haulmail.example

Font styles to use
Sans Serif

Colors
ec1f27
000000
cbcbcb
ffffff

Requirements
Must have
• Listed on the back, Earthworks | Haulage | Truck and Machinery Hire | Sand, Soil & Mulch Supply | Screening of Products
Nice to have
• Would be good for it to look appealing to a mans man, because it relates to heavy machinery, earthworks, construction etc. Black, red and white would be good maybe with a bit of silver somewhere.
Should not have
• not sure

```html
<!DOCTYPE html>
<html lang="en">
<head>
<meta charset="utf-8">
<title>Brolga Ridge Earthmoving &amp; Transport – Business Card</title>
<link href="https://fonts.googleapis.com/css2?family=Roboto:wght@400;500;700&display=swap" rel="stylesheet">
<style>
  :root {
    --backdrop: #1c1d20;
    --card: #050505;
    --silver: #8e8e90;
    --silver-soft: #6c6c6e;
    --silver-bright: #cbcbcb;
    --accent: #ec1f27;
  }
  * { margin: 0; padding: 0; box-sizing: border-box; }
  html, body { width: 1200px; height: 900px; overflow: hidden; }
  body {
    background: var(--backdrop);
    font-family: "Roboto", Arial, sans-serif;
    position: relative;
  }
  .card {
    position: absolute;
    width: 560px;
    height: 320px;
    background: var(--card);
    border-radius: 3px;
    box-shadow: 0 18px 40px rgba(0,0,0,0.55);
  }

  /* Shared name lockup: plain name with one square beside it */
  .lockup {
    display: flex;
    align-items: center;
    gap: 12px;
    color: var(--silver-bright);
    font-weight: 700;
    white-space: nowrap;
  }
  .lockup__square {
    flex: none;
    background: var(--accent);
  }

  /* Name side */
  .card--brand { left: 580px; top: 110px; }
  .card--brand .lockup {
    position: absolute;
    left: 0; right: 0; top: 118px;
    justify-content: center;
    font-size: 26px;
  }
  .card--brand .lockup__square { width: 24px; height: 24px; }
  .brand__rule {
    position: absolute;
    left: 150px; right: 150px; top: 180px;
    height: 2px;
    background: var(--accent);
  }
  .brand__abn {
    position: absolute;
    left: 0; right: 0; bottom: 70px;
    text-align: center;
    font-size: 17px;
    letter-spacing: 2px;
    color: var(--silver-soft);
  }

  /* Contact side */
  .card--contact { left: 70px; top: 470px; }
  .contact-person { position: absolute; left: 36px; top: 30px; }
  .contact-person__name {
    font-size: 26px;
    font-weight: 700;
    color: var(--silver-bright);
  }
  .contact-person__role {
    font-size: 13px;
    color: var(--silver-soft);
    padding-bottom: 6px;
    border-bottom: 1px solid var(--accent);
    display: inline-block;
    width: 170px;
  }
  .contact-list { position: absolute; left: 36px; top: 102px; list-style: none; }
  .contact-list li {
    display: flex; align-items: flex-start; gap: 12px;
    font-size: 14px; line-height: 1.35;
    color: var(--silver);
    margin-bottom: 8px;
  }
  .contact-list svg { flex: none; width: 20px; height: 20px; margin-top: 1px; }

  .card--contact .lockup {
    position: absolute;
    right: 30px; top: 32px;
    font-size: 15px;
    gap: 8px;
  }
  .card--contact .lockup__square { width: 12px; height: 12px; }

  .services {
    position: absolute;
    right: 24px; bottom: 22px;
    padding: 8px 16px;
    border: 2px solid var(--silver-soft);
    border-radius: 12px;
    font-size: 13px;
    font-weight: 500;
    line-height: 1.45;
    color: var(--silver);
  }
  .services__sep { color: var(--accent); }
</style>
</head>
<body>

  <section class="card card--brand" aria-label="Business card name side">
    <div class="lockup">
      <span class="lockup__square" aria-hidden="true"></span>
      <span>Brolga Ridge Earthmoving &amp; Transport</span>
    </div>
    <div class="brand__rule" aria-hidden="true"></div>
    <div class="brand__abn">ABN 52 907 338 214</div>
  </section>

  <section class="card card--contact" aria-label="Business card contact side">
    <div class="contact-person">
      <div class="contact-person__name">Dale Pettigrew</div>
      <div class="contact-person__role">Managing Director</div>
    </div>

    <div class="lockup">
      <span class="lockup__square" aria-hidden="true"></span>
      <span>Brolga Ridge</span>
    </div>

    <ul class="contact-list">
      <li>
        <svg viewBox="0 0 20 20" aria-hidden="true"><rect x="1" y="1" width="18" height="18" fill="none" stroke="#8e8e90" stroke-width="1.2"/><path d="M10 4.5a3.5 3.5 0 0 0-3.5 3.5c0 2.6 3.5 6.5 3.5 6.5s3.5-3.9 3.5-6.5A3.5 3.5 0 0 0 10 4.5z" fill="none" stroke="#ec1f27" stroke-width="1.2"/><circle cx="10" cy="8" r="1.2" fill="#ec1f27"/></svg>
        <span>42 CORELLA RISE<br>MARRALONG 6090<br>PERTH, WA</span>
      </li>
      <li>
        <svg viewBox="0 0 20 20" aria-hidden="true"><rect x="1" y="1" width="18" height="18" fill="none" stroke="#8e8e90" stroke-width="1.2"/><path d="M6 5l2 0 1 3-1.3 1a7 7 0 0 0 3.3 3.3l1-1.3 3 1v2a1 1 0 0 1-1 1A9 9 0 0 1 5 6a1 1 0 0 1 1-1z" fill="none" stroke="#ec1f27" stroke-width="1.2"/></svg>
        <span>0438 256 904</span>
      </li>
      <li>
        <svg viewBox="0 0 20 20" aria-hidden="true"><rect x="1" y="1" width="18" height="18" fill="none" stroke="#8e8e90" stroke-width="1.2"/><rect x="4.5" y="6" width="11" height="8" fill="none" stroke="#ec1f27" stroke-width="1.2"/><path d="M4.5 6l5.5 4.5L15.5 6" fill="none" stroke="#ec1f27" stroke-width="1.2"/></svg>
        <span>brgtransport2011@haulmail.example</span>
      </li>
    </ul>

    <div class="services">
      Earthworks <span class="services__sep">|</span> Haulage <span class="services__sep">|</span> Truck and Machinery Hire <span class="services__sep">|</span><br>
      Sand, Soil &amp; Mulch Supply <span class="services__sep">|</span> Screening of Products
    </div>
  </section>

</body>
</html>
```